Business Card Design

Hello Designer,
This is an internet based company. We specialize in low rate advertisement space on a number of our websites, Similar to roamjournal. We also Do keyword seo, social media development and management, website development,and mobile friendly reformatting of websites. The overall design should communicate Brightlane Links provides customers with easy access to our advertised businesses, to connect businesses to their desired customers and vice versa.
Updates

Hello Designers!,

If you would like to view my website for ideas please visit. sarasotaventro.example
Also I would like the "BRIGHTLANE LINKS" lettering to be different colors, like Zentros lettering. Also the color scheme I was thinking was blue, white, black
Thank you for taking on this project,
CorinĀ 

Industry/Entity Type

Internet

Contact Information for Business Card

Brightlane Links,Corin Mossfeld,CEO, corin@ventrowww.example, CELL: 941-555-0162, 4182 Larkspur Ln Sarasota 34231,corin@ventrowww.example, Making The Internet More Affordable and Manageable,sarasotaventro.example
ON BACK: Making The Internet More Affordable and Manageable, sarasotaventro,tampaventro,miamiventro,pensacolaventro,jacksonvilleventro, and more, many more.

```html
<!DOCTYPE html>
<html lang="en">
<head>
<meta charset="UTF-8">
<title>Brightlane Links — Business Card</title>
<link href="https://fonts.googleapis.com/css2?family=Michroma&family=Arimo:wght@400;700&display=swap" rel="stylesheet">
<style>
  :root {
    --page-bg: #e9e9ec;
    --card-light: #ffffff;
    --card-shade: #e4e4e8;
    --brand-blue: #3a3a9c;
    --ink: #2c2c3a;
    --on-blue: #ffffff;
  }
  * { box-sizing: border-box; margin: 0; padding: 0; }
  html, body { width: 1057px; height: 1200px; overflow: hidden; }
  body {
    background: var(--page-bg);
    font-family: "Arimo", Arial, sans-serif;
    position: relative;
  }
  .card {
    position: absolute;
    left: 108px;
    width: 840px;
    height: 480px;
    background: radial-gradient(ellipse at 45% 40%, var(--card-light) 0%, #f6f6f8 45%, var(--card-shade) 100%);
    box-shadow: 0 10px 30px rgba(0,0,0,0.18);
    overflow: hidden;
  }
  .card--front { top: 70px; }
  .card--back { top: 650px; }

  .brand-mark {
    font-family: "Michroma", "Arial Black", sans-serif;
    font-weight: 400;
    color: var(--brand-blue);
    font-variant: small-caps;
    letter-spacing: 0.16em;
    line-height: 1.25;
  }
  .card--front .brand-mark {
    position: absolute;
    left: 200px;
    top: 160px;
    font-size: 56px;
  }
  .card--front .brand-mark span { display: block; }
  .card--front .brand-mark span + span { padding-left: 60px; }

  .name-band {
    position: absolute;
    right: 0;
    top: 56px;
    width: 330px;
    height: 116px;
    background: var(--brand-blue);
    color: var(--on-blue);
    text-align: center;
    padding-top: 26px;
  }
  .name-band .person-name {
    font-size: 28px;
    letter-spacing: 0.06em;
    text-transform: uppercase;
  }
  .name-band .person-role {
    margin-top: 8px;
    font-size: 16px;
    letter-spacing: 0.08em;
    text-transform: uppercase;
  }

  .card--back .brand-mark {
    position: absolute;
    left: 56px;
    top: 206px;
    font-size: 30px;
  }

  .contact-list {
    position: absolute;
    left: 56px;
    top: 270px;
    list-style: none;
  }
  .contact-list li {
    display: flex;
    align-items: center;
    gap: 14px;
    height: 34px;
    font-size: 15px;
    color: var(--ink);
  }
  .contact-icon {
    width: 22px;
    height: 22px;
    flex: none;
  }
</style>
</head>
<body>

<section class="card card--front" aria-label="Card front">
  <h1 class="brand-mark"><span>Brightlane</span><span>Links</span></h1>
</section>

<section class="card card--back" aria-label="Card back">
  <div class="name-band">
    <p class="person-name">Jonah Pell</p>
    <p class="person-role">Founder</p>
  </div>

  <h2 class="brand-mark">Brightlane Links</h2>

  <ul class="contact-list">
    <li>
      <svg class="contact-icon" viewBox="0 0 22 22" aria-hidden="true">
        <rect width="22" height="22" fill="#3a3a9c"/>
        <path d="M7 5h3l1 3-2 1.5a8 8 0 0 0 3.5 3.5L14 11l3 1v3c0 1-1 2-2 2A11 11 0 0 1 5 7c0-1 1-2 2-2z" fill="#fff"/>
      </svg>
      <span>012 555 0147</span>
    </li>
    <li>
      <svg class="contact-icon" viewBox="0 0 22 22" aria-hidden="true">
        <rect width="22" height="22" fill="#3a3a9c"/>
        <rect x="7" y="4" width="8" height="14" rx="1.5" fill="#fff"/>
        <rect x="8.5" y="6" width="5" height="8" fill="#3a3a9c"/>
      </svg>
      <span>012 555 0147</span>
    </li>
    <li>
      <svg class="contact-icon" viewBox="0 0 22 22" aria-hidden="true">
        <rect width="22" height="22" fill="#3a3a9c"/>
        <rect x="4" y="6" width="14" height="10" fill="#fff"/>
        <path d="M4 6l7 5 7-5" fill="none" stroke="#3a3a9c" stroke-width="1.5"/>
      </svg>
      <span>yourname@mail.example</span>
    </li>
    <li>
      <svg class="contact-icon" viewBox="0 0 22 22" aria-hidden="true">
        <rect width="22" height="22" fill="#3a3a9c"/>
        <circle cx="11" cy="11" r="6" fill="none" stroke="#fff" stroke-width="1.5"/>
        <path d="M5 11h12M11 5c-3 3-3 9 0 12M11 5c3 3 3 9 0 12" fill="none" stroke="#fff" stroke-width="1.2"/>
      </svg>
      <span>www.yoursite.example</span>
    </li>
    <li>
      <svg class="contact-icon" viewBox="0 0 22 22" aria-hidden="true">
        <rect width="22" height="22" fill="#3a3a9c"/>
        <path d="M11 4a5 5 0 0 1 5 5c0 4-5 9-5 9s-5-5-5-9a5 5 0 0 1 5-5z" fill="#fff"/>
        <circle cx="11" cy="9" r="2" fill="#3a3a9c"/>
      </svg>
      <span>5260 Elm Ridge Avenue, Suite 12</span>
    </li>
  </ul>
</section>

</body>
</html>
```